Harrow WordPress Design Contest

We need a wordpress design that will incorporate a professional color scheme with company logo in a clean layout. The design needs to consider that this will be developed on a responsive theme. Colors are up to the designer - The green of the logo with black, gray or an accent color. Client wants a 'modern' look.

Industry/Entity Type

It Company

Number of Pages Required

1 page

Font styles to use
Serif
Sans Serif

Requirements
Must have
• Navigation: 1) Home 2) All Auctions 3) Real Estate for Sale 4) Services 5) About Us 6) Contact Us
• Colors - a corporate look with professional color scheme. Green of logo + black and gray, or an eggshell/light beige, or any other accent that keeps within a corporate look.
• In header - logo (attached) , and contact info :5127 Old Tenbury Lane, Scottsville, KY 42190
• 270-555-0143
• Fax: 270-555-0179
• Email:info@harrowlandbidhouse.example
• Design will feature a full width (960 px) slideshow - use a stock photo for real estate.
• Widgets in sidebar or where appropriate - 1) Email Signup 2) Message of the Day 3) Upcoming Auctions 4) News&Events blog 5) Testimonials 6) Social media - QX, chirpo, vidloop, snapboard, zentro+
• Footer will have company logo, association logos (attached) and contact info, with another widget area if necessary
Nice to have
• use of drop down menu styling - Upcoming Auctions / Online Auctions/ Past Auctions under the "Auction Calendar" menu item

```html
<!DOCTYPE html>
<html lang="en">
<head>
<meta charset="utf-8">
<title>Harrow Real Estate &amp; Auction Co.</title>
<link href="https://fonts.googleapis.com/css2?family=Open+Sans:ital,wght@0,400;0,600;1,400&display=swap" rel="stylesheet">
<style>
:root{
  --green:#17612a;
  --green-dark:#0e3d1a;
  --green-text:#1d6a31;
  --ink:#333;
  --muted:#999;
  --line:#e3e3e3;
  --band:#efefef;
  --footer:#2b2b2b;
  --footer-deep:#1f1f1f;
  --footer-text:#cfcfcf;
}
*{box-sizing:border-box;margin:0;padding:0}
html,body{width:731px;height:1200px;overflow:hidden;background:#fff}
body{font-family:"Open Sans",Arial,sans-serif;color:var(--ink);position:relative}
.abs{position:absolute}

.brand{left:72px;top:30px;display:flex;align-items:center;gap:10px}
.brand-mark{width:34px;height:34px;background:var(--green)}
.brand-name{font-size:24px;font-weight:600;color:var(--green);line-height:1}
.contact{right:73px;top:25px;text-align:right;font-size:9px;line-height:14px}
.contact .big{font-size:10.5px;color:var(--green-text);line-height:16px}

.nav{left:66px;top:96px;width:599px;height:31px;background:var(--green);display:flex;z-index:2}
.nav a{color:#fff;text-decoration:none;font-size:9px;display:flex;align-items:center;justify-content:center;border-right:1px solid rgba(255,255,255,.18)}
.nav a:last-child{border-right:0}
.nav a.active{background:var(--green-dark)}

.hero{left:0;top:111px;width:731px;height:318px;background:linear-gradient(180deg,#b9c7d4 0%,#d9dfe4 35%,#a3865a 55%,#6f6559 80%,#555 100%)}
.hero-prev{left:0;top:258px;width:19px;height:24px;background:rgba(80,80,80,.7)}

.section-title{font-size:11.5px;color:var(--green-text);font-weight:400}
.auctions-title{left:73px;top:452px}
.auction-next{left:477px;top:456px}
.card{width:129px}
.card .photo{width:129px;height:87px}
.card h3{font-size:8.5px;font-weight:400;line-height:12.5px;margin-top:8px;color:#333}
.card p{font-size:7px;line-height:11px;color:var(--muted);margin-top:4px}

.news-title{left:513px;top:452px}
.news{left:513px;top:480px;width:145px;border:1px solid var(--line)}
.news-item{height:76.5px;padding:12px 17px 0;border-bottom:1px solid var(--line)}
.news-item h4{font-size:8.5px;font-weight:400;color:#444}
.news-item p{font-size:6.3px;line-height:11px;color:var(--muted);margin-top:4px}
.news-more{height:13px;background:#eee;font-size:8px;padding-left:18px;line-height:13px}

.testimonials{left:0;top:824px;width:731px;height:156px;background:var(--band);border-top:1px solid #ddd}
.testimonials h2{position:absolute;top:24px;width:100%;text-align:center;font-size:17.5px;font-weight:600;color:var(--green)}
.avatar{left:83px;top:59px;width:74px;height:74px;border-radius:50%;border:3px solid #fff;background:radial-gradient(circle,#d8b49c,#bfc6cc);box-shadow:0 1px 3px rgba(0,0,0,.25)}
.quote{left:169px;top:65px;width:485px;font-size:8.4px;line-height:14.5px;font-style:italic;color:#444}
.quote cite{display:block;margin-top:4px;font-style:normal;color:var(--green-text);font-size:8.5px}

.footer{left:0;top:980px;width:731px;height:173px;background:var(--footer)}
.footer .col-rule{position:absolute;top:20px;width:1px;height:134px;background:#444}
.f-links{left:73px;top:19px;list-style:none;font-size:8px;color:var(--footer-text)}
.f-links li{height:24px}
.f-links li::before{content:"•";margin-right:5px}
.f-head{font-size:9px;color:#5fae6e}
.f-msg{left:190px;top:19px;width:160px}
.f-msg h5{font-size:9.5px;font-weight:400;color:#ddd;margin-top:9px}
.f-msg p{font-size:7px;line-height:12.5px;color:#888;margin-top:5px}
.f-msg .more{font-size:7.5px;color:#ddd;margin-top:13px;font-weight:600}
.f-news{left:388px;top:19px}
.signup{display:flex;margin-top:14px}
.signup span{width:105px;height:26px;background:#fff;border-radius:2px 0 0 2px;font-size:7.5px;color:#777;padding:8px 10px}
.signup b{width:54px;height:26px;background:#555;color:#fff;font-size:7.5px;font-weight:400;display:flex;align-items:center;justify-content:center;border-radius:0 2px 2px 0}
.follow{margin-top:23px}
.socials{display:flex;gap:6px;margin-top:8px}
.socials i{width:19px;height:19px;border-radius:50%;background:#555;display:block}
.f-aff{left:599px;top:19px}
.badge{width:56px;height:22px;background:#f4f4f4;margin-top:12px;border-radius:2px}
.badge.round{border-radius:50%;height:26px;background:#777}

.bottom{left:0;top:1153px;width:731px;height:47px;background:var(--footer-deep);font-size:7.2px;color:#888}
.bottom .copy{position:absolute;left:73px;top:19px}
.bottom .legal{position:absolute;right:73px;top:19px}
</style>
</head>
<body>

<header>
  <div class="abs brand">
    <span class="brand-mark"></span>
    <span class="brand-name">Harrow</span>
  </div>
  <div class="abs contact">
    5127 Old Tenbury Lane, Scottsville, KY 42190<br>
    Fax : 270-555-0179<br>
    <span class="big">Phone : 270-555-0143</span><br>
    <span class="big">Email : info@harrowlandbidhouse.example</span>
  </div>
  <nav class="abs nav">
    <a class="active" href="#" style="width:71px">HOME</a>
    <a href="#" style="width:110px">ALL AUCTIONS</a>
    <a href="#" style="width:142px">REAL ESTATE FOR SALE</a>
    <a href="#" style="width:89px">SERVICES</a>
    <a href="#" style="width:91px">ABOUT US</a>
    <a href="#" style="width:96px">CONTACT US</a>
  </nav>
</header>

<div class="abs hero" role="img" aria-label="Slideshow photo of a large mining truck and excavator on a rocky site under a cloudy sky"></div>
<div class="abs hero-prev"><svg width="19" height="24" viewBox="0 0 19 24"><path d="M12 6 L6 12 L12 18" fill="none" stroke="#fff" stroke-width="1.5"/></svg></div>

<main>
  <h2 class="abs section-title auctions-title">Upcoming Auctions</h2>
  <svg class="abs auction-next" width="11" height="11" viewBox="0 0 11 11"><circle cx="5.5" cy="5.5" r="5.5" fill="#aaa"/><path d="M4.5 3 L7.5 5.5 L4.5 8Z" fill="#fff"/></svg>

  <article class="abs card" style="left:73px;top:480px">
    <div class="photo" role="img" aria-label="Green pasture with hills and blue sky" style="background:linear-gradient(180deg,#8fb3d6 0%,#cfdbe6 40%,#4f8a2c 60%,#2f6418 100%)"></div>
    <h3>Phasellus nisl est, condimen tum vitae</h3>
    <p>Quisque aliquet ex nec est vestib-ulum pulvinar</p>
  </article>
  <article class="abs card" style="left:215px;top:480px">
    <div class="photo" role="img" aria-label="Plowed farm field with green crop rows" style="background:linear-gradient(180deg,#4a86c9 0%,#8fb9e0 25%,#5aa033 45%,#8a5a34 75%,#6b3f22 100%)"></div>
    <h3>Aenean sed quam non sapien faucibus</h3>
    <p>Quisque aliquet ex nec est vestib-ulum pulvinar</p>
  </article>
  <article class="abs card" style="left:358px;top:480px">
    <div class="photo" role="img" aria-label="Farm field with wooden fence under a deep blue sky" style="background:linear-gradient(180deg,#1f3d7a 0%,#5a7fb8 45%,#6a9a3a 65%,#3f6a20 100%)"></div>
    <h3>Proin porta fermentum ipsum, vel porttitor</h3>
    <p>Quisque aliquet ex nec est vestib-ulum pulvinar</p>
  </article>
  <article class="abs card" style="left:73px;top:649px">
    <div class="photo" role="img" aria-label="Aerial view of contour farmland by a lake" style="background:linear-gradient(180deg,#6a9fb0 0%,#3f8a3a 35%,#2f6a22 70%,#5a8a2a 100%)"></div>
    <h3>Mauris suscipit felis id nunc elementum varius</h3>
    <p>Quisque aliquet ex nec est vestib-ulum pulvinar</p>
  </article>
  <article class="abs card" style="left:215px;top:649px">
    <div class="photo" role="img" aria-label="Green farm tractor with yellow wheels" style="background:linear-gradient(180deg,#6a9ad0 0%,#a9c7e8 40%,#2f6a1e 55%,#c9a030 85%,#8a6a2a 100%)"></div>
    <h3>Phasellus blandit quam a ipsum gravida</h3>
    <p>Quisque aliquet ex nec est vestib-ulum pulvinar</p>
  </article>
  <article class="abs card" style="left:358px;top:649px">
    <div class="photo" role="img" aria-label="Silver pickup truck on gravel" style="background:linear-gradient(180deg,#9fb2c4 0%,#c9d2da 35%,#8a8f94 65%,#6b6460 100%)"></div>
    <h3>Praesent iaculis faucibus urna sit amet lacinia</h3>
    <p>Quisque aliquet ex nec est vestib-ulum pulvinar</p>
  </article>

  <h2 class="abs section-title news-title">Latest News</h2>
  <aside class="abs news">
    <div class="news-item"><h4>Pnteger eu massa lacinia</h4><p>Praesent quis risus mi. In mollis nulla in pulvinar dictum. Vivamus interdum sagittis felis.</p></div>
    <div class="news-item"><h4>Pnteger eu massa lacinia</h4><p>Praesent quis risus mi. In mollis nulla in pulvinar dictum. Vivamus interdum sagittis felis.</p></div>
    <div class="news-item"><h4>Pnteger eu massa lacinia</h4><p>Praesent quis risus mi. In mollis nulla in pulvinar dictum. Vivamus interdum sagittis felis.</p></div>
    <div class="news-item"><h4>Pnteger eu massa lacinia</h4><p>Praesent quis risus mi. In mollis nulla in pulvinar dictum. Vivamus interdum sagittis felis.</p></div>
    <div class="news-more">››</div>
  </aside>
</main>

<section class="abs testimonials">
  <h2>TESTIMONIALS</h2>
  <svg class="abs" style="left:30px;top:70px" width="12" height="20" viewBox="0 0 12 20"><path d="M10 2 L2 10 L10 18" fill="none" stroke="#777" stroke-width="1.6"/></svg>
  <svg class="abs" style="left:688px;top:70px" width="12" height="20" viewBox="0 0 12 20"><path d="M2 2 L10 10 L2 18" fill="none" stroke="#777" stroke-width="1.6"/></svg>
  <div class="abs avatar" role="img" aria-label="Portrait of the client giving the testimonial"></div>
  <blockquote class="abs quote">“ Nam a malesuada libero. Duis sodales et libero vel interdum. Interdum et malesuada fames ac ante ipsum primis in faucibus. Donec lobortis dui tortor, eu lobortis felis mattis nec. Sed justo quam, luctus eu mauris eget, euismod dapibus sem. Sed tempus feugiat ante, at ornare libero volutpat sed. Maecenas quis magna magna. ”
    <cite>Dana Whitlock, NY</cite>
  </blockquote>
</section>

<footer class="abs footer">
  <span class="col-rule" style="left:171px"></span>
  <span class="col-rule" style="left:365px"></span>
  <span class="col-rule" style="left:573px"></span>
  <ul class="abs f-links">
    <li>Home</li><li>All Auctions</li><li>Real Estate for Sale</li><li>Services</li><li>About Us</li><li>Contact Us</li>
  </ul>
  <div class="abs f-msg">
    <div class="f-head">Message of the Day</div>
    <h5>Pellentesque convallis molestie</h5>
    <p>Aenean placerat, nibh vel accumsan aliquet, magna nibh accumsan nibh, ac tempus nunc ipsum ac tellus. Cras augue magna, placerat eget nulla non, congue suscipit neque. Sed libero felis, vestibulum et dolor eget.</p>
    <div class="more">MORE</div>
  </div>
  <div class="abs f-news">
    <div class="f-head">Newsletter Subscribe</div>
    <div class="signup"><span>E-mail Address</span><b>Subscribe</b></div>
    <div class="f-head follow">Follow us on :</div>
    <div class="socials" aria-label="Social links: QX, chirpo, zentro+, snapboard, vidloop, email">
      <i title="QX"></i><i title="chirpo"></i><i title="zentro+"></i><i title="snapboard"></i><i title="vidloop"></i>
      <svg width="19" height="19" viewBox="0 0 19 19"><circle cx="9.5" cy="9.5" r="9.5" fill="#4d9a3c"/><rect x="5" y="6" width="9" height="7" fill="#fff"/><path d="M5 6 L9.5 10 L14 6" fill="none" stroke="#4d9a3c" stroke-width="1"/></svg>
    </div>
  </div>
  <div class="abs f-aff">
    <div class="f-head">Affiliations</div>
    <div class="badge" aria-label="Association badge"></div>
    <div class="badge" aria-label="Listing service badge"></div>
    <div class="badge round" aria-label="State association badge"></div>
  </div>
</footer>

<div class="abs bottom">
  <span class="copy">Copyright © 2015 Harrow Real Estate Auction. &nbsp; All rights reserved.</span>
  <span class="legal">Terms &amp; Conditions Privacy &amp; Disclaimer Returns &amp; Refunds</span>
</div>

</body>
</html>
```